Brisca Coffee Cups

We already have Brisca Coffee cups, but the existing design is dated.
It needs a fresh modern look. (this look will be used with all Brisca advertising..
But the look and font of the word Brisca needs to say the same.

Industry/Entity Type

Advertising

```html
<!DOCTYPE html>
<html lang="en">
<head>
<meta charset="utf-8">
<title>Brisca Coffee Cup Wrap</title>
<link rel="stylesheet" href="https://fonts.googleapis.com/css2?family=Open+Sans:wght@400;600&display=swap">
<style>
  :root {
    --mint: #cbe9e3;
    --mint-pattern: #c4e4de;
    --brown: #7a300c;
    --brown-dark: #6e2b08;
    --white: #ffffff;
    --dieline: #e8d24a;
    --page: #ffffff;
  }
  html, body {
    margin: 0;
    padding: 0;
    width: 1200px;
    height: 671px;
    overflow: hidden;
    background: var(--page);
  }
  .cup-wrap {
    display: block;
    width: 1200px;
    height: 671px;
  }
  .brand-name {
    font-family: "Open Sans", sans-serif;
    font-weight: 600;
    font-size: 84px;
    fill: var(--brown);
  }
  .web-address {
    font-family: "Open Sans", sans-serif;
    font-weight: 400;
    font-size: 19px;
    fill: var(--brown);
  }
  .order-label {
    font-family: "Open Sans", sans-serif;
    font-weight: 400;
    font-size: 9.5px;
    fill: var(--white);
  }
  .order-box { fill: var(--white); }
  .pattern-area { fill: var(--mint-pattern); }
  .plain-band { fill: var(--mint); }
  .band-rule { fill: none; stroke: var(--white); }
  .logo-ring { fill: var(--white); }
  .logo-field { fill: var(--mint); }
  .order-strip { fill: var(--brown-dark); }
  .dieline {
    fill: none;
    stroke: var(--dieline);
    stroke-width: 1;
    stroke-dasharray: 4 3;
  }
</style>
</head>
<body>
<svg class="cup-wrap" viewBox="0 0 1200 671" xmlns="http://www.w3.org/2000/svg">
  <defs>
    <clipPath id="wrap-shape">
      <path d="M0,100 Q600,-70 1200,100 L1060,668 Q600,545 140,668 Z"/>
    </clipPath>
  </defs>

  <g clip-path="url(#wrap-shape)">
    <!-- doodle pattern background -->
    <rect class="pattern-area" x="0" y="0" width="1200" height="671"
          role="img" aria-label="Repeating line-drawn doodles of coffee cups, takeaway cups, croissants, cupcakes, hearts, coffee beans and speech bubbles reading coffee, in brown on mint"/>

    <!-- lower plain band -->
    <path class="plain-band" d="M0,545 Q600,435 1200,545 L1200,671 L0,671 Z"/>
    <path class="band-rule" stroke-width="9" d="M0,545 Q600,435 1200,545"/>
    <path class="band-rule" stroke-width="14" d="M0,600 Q600,490 1200,600"/>
    <path class="pattern-area" d="M0,640 Q600,530 1200,640 L1200,671 L0,671 Z"
          role="img" aria-label="Continuation of the coffee doodle pattern"/>

    <!-- logo ovals -->
    <g transform="rotate(-5 335 290)">
      <ellipse class="logo-ring" cx="335" cy="290" rx="200" ry="112"/>
      <ellipse class="logo-field" cx="335" cy="290" rx="186" ry="99"/>
      <text class="brand-name" x="335" y="318" text-anchor="middle">brisca</text>
    </g>
    <g transform="rotate(5 945 290)">
      <ellipse class="logo-ring" cx="945" cy="290" rx="200" ry="112"/>
      <ellipse class="logo-field" cx="945" cy="290" rx="186" ry="99"/>
      <text class="brand-name" x="945" y="318" text-anchor="middle">brisca</text>
    </g>

    <!-- web addresses -->
    <text class="web-address" x="385" y="560" text-anchor="middle" transform="rotate(-4 385 560)">briscacoffee.com.au</text>
    <text class="web-address" x="838" y="560" text-anchor="middle" transform="rotate(4 838 560)">briscacoffee.com.au</text>

    <!-- order strip -->
    <rect class="order-strip" x="553" y="0" width="102" height="671"/>

    <!-- dieline -->
    <path class="dieline" d="M15,110 Q600,-50 1185,110 L1050,650 Q600,530 150,650 Z"/>
  </g>

  <!-- order checklist -->
  <g class="order-list">
    <text class="order-label" x="588" y="243" text-anchor="end">cap</text>
    <circle class="order-box" cx="625" cy="240" r="7"/>
    <text class="order-label" x="588" y="274" text-anchor="end">latte</text>
    <circle class="order-box" cx="625" cy="271" r="7"/>
    <text class="order-label" x="606" y="304" text-anchor="end">flat white</text>
    <circle class="order-box" cx="625" cy="301" r="7"/>
    <text class="order-label" x="606" y="335" text-anchor="end">long black</text>
    <circle class="order-box" cx="625" cy="332" r="7"/>
    <text class="order-label" x="597" y="366" text-anchor="end">mocha</text>
    <circle class="order-box" cx="625" cy="363" r="7"/>
    <text class="order-label" x="590" y="397" text-anchor="end">choc</text>
    <circle class="order-box" cx="625" cy="394" r="7"/>
    <text class="order-label" x="592" y="428" text-anchor="end">decaf</text>
    <circle class="order-box" cx="625" cy="425" r="7"/>
    <text class="order-label" x="585" y="459" text-anchor="end">soy</text>
    <circle class="order-box" cx="625" cy="456" r="7"/>
    <text class="order-label" x="594" y="489" text-anchor="end">sugar</text>
    <circle class="order-box" cx="625" cy="486" r="7"/>
  </g>
</svg>
</body>
</html>
```